Hole-in-the-wall Food Kiosk Flyer

We would like to outsource a flyer design.

CLIENT: Parolcito Lechon + Wraps
DESCRIPTION: Food Take-out and Delivery

PROJECT GOAL:
- To be able to make a flyer that showcases the company intro and its menu.
- The purpose of this flyer is for customers to be able to keep it and take it out whenever they feel the need to order some food.

------------------------------------------------------------------------------------
CLIENT DESCRIPTION:

Parolcito is a hole-in-the-wall food kiosk specializing in Mexican-inspired Filipino food.

Our menu booasts a delectable range of Filipino favorites such as sisig and rice meals meshed with some well-loved Mexican flair. Crispy Sisig in Toasted Tacos, anyone?

We pride ourselves in serving familiar, close-to-home savor with a minor twist. So if you're hungry for comfort food, but can't quite put your finger on what, come to Parolcito for food that hits the spot.

BRAND IMAGE:
- Fun, Non-intimidating, Rustic, Homey

https://www.snapgallerio.com/parolcito_lechonwraps/

FOOD MENU:

A. SISIG
- Crispy Sisig
- Chicken Adobo Sisig
* Can be served as: 1) Rice Meal 2) Taco 3) Burrito 4) For Sharing of 2-3 persons.
* Prices are different for each format (If it's a rice meal, taco, etc.)

B. CRISPY SINIGANG
- rice meal
- for sharing

C. BEEF STEAK
- burrito
- taco

D. CRISPY CHICKEN WINGS
- rice meal
- for sharing

E. ULTIMATE NACHOS

F. BLACK TAPA
- rice meal served with egg

G. BEEF BURGER
- as a rice meal served with egg
- or served in a bun.

H. DRINKS
- Vento Iced Tea
- Bottled Water

We included some photos and the logo to give you inspiration.

Thanks!

Target Market(s)

- Young Adults, aged 18-32, working/residing in Rockwell Area, Makati City Philippines.
- They are open to new ideas/willing to try new things.
- They are a bit budget conscious. They want delicious, home-feel food.
- They are avid social media subscribers. They are mostly online.

Industry/Entity Type

Food Store

Colors
f37122
9bcb3b
ffc214

Requirements
Must have
• THINGS TO THINK ABOUT:
• - Final size should be 3.85"x8.85". This can be a folded size or a spread out size. The idea is for it to fit most mailboxes with ease.
• - Contact info must include, celphone, facebook, and instagram.
• - Flyer has to be appetizing and appealing. Make use of food photos.
Nice to have
• - The flyer should be useful in some other manner rather than just being a menu flyer. (Maybe it can also be a ruler, etc.)
• - Colors can be up to you.

```html
<!DOCTYPE html>
<html lang="en">
<head>
<meta charset="utf-8">
<title>Parolcito Lechon + Wraps – Menu Flyer</title>
<link rel="stylesheet" href="https://fonts.googleapis.com/css2?family=Luckiest+Guy&family=Special+Elite&family=Sniglet:wght@800&family=Oswald:wght@700&display=swap">
<style>
  :root {
    --stage: #1f2628;
    --paper-light: #d8ccb1;
    --paper-mid: #c4b597;
    --paper-dark: #a89a7c;
    --ink: #3b3833;
    --menu-green: #8cf527;
    --heading-shade: #2f4a0f;
    --accent-orange: #e8561b;
    --brand-yellow: #ffc214;
    --frame-dark: #2c2a26;
    --white: #ffffff;
  }
  * { margin: 0; padding: 0; box-sizing: border-box; }
  html, body { width: 1200px; height: 1000px; overflow: hidden; background: var(--stage); }
  .canvas { position: relative; width: 1200px; height: 1000px; background: var(--stage); }

  .flyer {
    position: absolute; left: 144px; top: 32px; width: 408px; height: 938px;
    overflow: hidden;
  }
  .paper {
    position: absolute; inset: 0;
    background: linear-gradient(170deg, var(--paper-light) 0%, var(--paper-mid) 45%, var(--paper-dark) 100%);
  }
  .frame { position: absolute; inset: 0; }

  .brand-name {
    position: absolute; left: 20px; top: 92px;
    font-family: "Special Elite", monospace; font-size: 62px; line-height: 1;
    color: var(--frame-dark); letter-spacing: 1px;
  }
  .brand-tagline {
    position: absolute; right: 26px; top: 158px;
    font-family: "Special Elite", monospace; font-size: 13px; color: var(--ink);
  }

  .menu-heading {
    position: absolute;
    font-family: "Luckiest Guy", cursive; font-size: 19px; letter-spacing: 0.5px;
    color: var(--menu-green);
    text-shadow: 1px 1px 0 var(--heading-shade), -1px 0 0 var(--heading-shade);
  }
  .menu-line {
    position: absolute;
    font-family: "Special Elite", monospace; font-size: 12.5px; line-height: 14px;
    text-transform: uppercase; letter-spacing: 1px; color: var(--ink);
    white-space: pre;
  }
  .menu-line.featured { color: var(--accent-orange); }
  .format-note {
    position: absolute; left: 244px; top: 206px;
    font-family: "Special Elite", monospace; font-size: 10.5px; line-height: 12.5px;
    text-transform: uppercase; letter-spacing: 0.8px; color: var(--ink); white-space: pre;
  }

  .social {
    position: absolute; display: flex; align-items: center; gap: 6px;
    transform-origin: left top; transform: rotate(-90deg);
    font-family: "Special Elite", monospace; font-size: 12px; color: var(--frame-dark);
    white-space: nowrap;
  }
  .social-mark { width: 12px; height: 12px; border: 2px solid var(--frame-dark); }
  .social-mark.round { border-radius: 50%; }

  .order-title {
    position: absolute; left: 34px; top: 828px; width: 340px;
    font-family: "Sniglet", sans-serif; font-weight: 800; font-size: 23px; letter-spacing: 1.5px;
    color: var(--white); text-shadow: 1px 1px 0 var(--frame-dark);
  }
  .order-phone {
    position: absolute; left: 0; top: 856px; width: 408px; text-align: center;
    font-family: "Oswald", sans-serif; font-weight: 700; font-size: 20px; letter-spacing: 1px;
    color: var(--menu-green); text-shadow: 1px 1px 0 var(--heading-shade);
  }
  .order-address {
    position: absolute; left: 0; top: 884px; width: 408px; text-align: center;
    font-family: "Oswald", sans-serif; font-weight: 700; font-size: 13px; line-height: 15px;
    color: var(--accent-orange); text-transform: uppercase; text-shadow: 1px 1px 0 var(--frame-dark);
  }
  .order-hashtag {
    position: absolute; left: 0; top: 916px; width: 408px; text-align: center;
    font-family: "Oswald", sans-serif; font-weight: 700; font-size: 13px;
    color: var(--paper-light); text-shadow: 1px 1px 0 var(--frame-dark);
  }
</style>
</head>
<body>
<main class="canvas">
  <article class="flyer">
    <div class="paper" role="img" aria-label="Aged kraft paper texture with faint dotted pattern"></div>

    <svg class="frame" width="408" height="938" viewBox="0 0 408 938" aria-hidden="true">
      <defs>
        <linearGradient id="frameGrad" x1="0" y1="140" x2="0" y2="915" gradientUnits="userSpaceOnUse">
          <stop offset="0" stop-color="#e8561b"/>
          <stop offset="0.3" stop-color="#ffc214"/>
          <stop offset="0.6" stop-color="#9bf02a"/>
          <stop offset="0.85" stop-color="#2f4a0f"/>
          <stop offset="1" stop-color="#2c2a26"/>
        </linearGradient>
      </defs>
      <g fill="none" stroke="url(#frameGrad)" stroke-width="5" stroke-dasharray="9 5">
        <path d="M34 140 H8 V912 H400 V140 H378"/>
      </g>
    </svg>

    <div class="brand-name">Parolcito</div>
    <div class="brand-tagline">lechon + wrap shop</div>

    <div class="menu-heading" style="left:40px;top:200px">Sisig</div>
    <div class="menu-line featured" style="left:40px;top:231px">•Crispy Sisig</div>
    <div class="menu-line featured" style="left:40px;top:250px">•Chicken Adobo Sisig</div>
    <div class="format-note">-Rice Meal
-Taco
-Burrito
-For Sharing
(2-3Persons)
*Food Prices Vary*</div>

    <div class="menu-heading" style="left:40px;top:298px">Black Tapa</div>
    <div class="menu-line" style="left:30px;top:325px">      -Rice Meal
(Served w/ Egg)</div>

    <div class="menu-heading" style="left:40px;top:368px">Beef Steak</div>
    <div class="menu-line" style="left:60px;top:394px">-Burrito
  -Taco</div>

    <div class="menu-heading" style="left:40px;top:440px">Ultimate Nachos</div>

    <div class="menu-heading" style="left:40px;top:483px">Beef Burger</div>
    <div class="menu-line" style="left:44px;top:510px">   -Rice Meal
(Served W/Egg)
     -Bun</div>

    <div class="menu-heading" style="left:36px;top:577px">Crispy Chicken Wings</div>
    <div class="menu-line" style="left:60px;top:604px">-Rice Meal
-For Sharing</div>

    <div class="menu-heading" style="left:40px;top:643px">Crispy Sinigang</div>
    <div class="menu-line" style="left:60px;top:669px">-Rice Meal
-For Sharing</div>

    <div class="menu-heading" style="left:40px;top:727px">Drinks</div>
    <div class="menu-line" style="left:40px;top:759px">•Vento Iced Tea</div>
    <div class="menu-line" style="left:40px;top:780px">•Bottled Water</div>

    <div class="social" style="left:352px;top:620px">
      <span class="social-mark"></span><span>parolcito lechon wrap shop</span>
    </div>
    <div class="social" style="left:352px;top:800px">
      <span class="social-mark round"></span><span>@parolcito_lechonwraps</span>
    </div>

    <div class="order-title">take out and delivery</div>
    <div class="order-phone">+63900 555 0142</div>
    <div class="order-address">12 Sampaguita Street, Lunaria Village<br>Makati City, 1200</div>
    <div class="order-hashtag">#parolcitolechonwraps</div>
  </article>
</main>
</body>
</html>
```